Event website for the Brisk industry

brisk! is a new show in the Australian market so the website needs to be informative, easy to navigate and clear as to what the event is about and why they should attend – needs to be professional but still fun and dynamic.

Imagery needs to be colourful, fresh, inviting, and should involve a mixture of close up food shots with shots of people interacting.
The event’s competitions are fun and a little quirky (the “Toastathon” and “Blender Contest”), so creative should represent this in tone.

brisk! is a niche and unique show aimed at the multi-million dollar food-to-go market in Australia.
Key selling points for visitors:
- Discover the latest products (food and beverage lines) and equipment to hit the market
- Network with their peers
- Immerse themselves in a range of fun and interactive features – see attached list.
Key selling points for exhibitors:
- Speak directly to decision makers from small – large, food to go related businesses.
- Small niche show, exhibitors have more of an opportunity to stand out/ limited size so good variety of products on display

Some examples of Australian websites which are targeting the same type of customer:
http://www.wrapguild.org.au/ - clean/bright/simple
www.platterexpoaus.com.au – we like the simplicity of the Platter Expo website – very clean/colourful.
Updates

Hi All, 

Thanks for the interest in our competition, I will be away until the 11th of January at which point i will comment on the designs. 

Thanks and Merry Xmas. 

Target Market(s)

Café/Restaurant owners Sandwich bars/Juice Bars/Bakeries/Delis/Gourmet food stores Pubs/Clubs/Contract Caterers Supermarkets/Food Wholesalers

Industry/Entity Type

Industry

Requirements
Must have
• Main objectives:
1. Visitor Registration – call to action to "Register Now" needs to be very prominent on the home page and on the pages throughout the website
2. Information on exhibiting "Want to Exhibit" – needs to be clearly available.
3. Being a new show, data capture is important, so this needs to feature on the home page.
4. Social Media share buttons
5. Floating CSS Nav bar (top or bottom) with key call to actions - Register, Want to exhibit?, sign up

I would like all designs to have both a home page and a content page submitted.
Should not have
• Brisk UK show website: www.briskshow.co.uk
- We will be using the same branding as the UK brisk show website but we don’t like how busy their website is (too many blocks of run on text and too many navigation tiles on the home page). We would prefer to take a more simplified approach – ie. hero images (JQuery) dominating the screen, with a really strong CTA to register and to find out more about exhibiting.

```html
<!DOCTYPE html>
<html lang="en">
<head>
<meta charset="utf-8">
<title>brisk! – The contemporary food to go show</title>
<link href="https://fonts.googleapis.com/css2?family=Arimo:ital,wght@0,400;0,700;1,400&family=Roboto+Condensed:wght@400&display=swap" rel="stylesheet">
<style>
:root{
  --lime:#9cc43a;
  --lime-soft:#dde48a;
  --ink:#111;
  --white:#fff;
  --rule:#dcdcdc;
}
*{margin:0;padding:0;box-sizing:border-box}
html,body{width:1176px;height:1200px;overflow:hidden;background:var(--white)}
body{position:relative;font-family:Arimo,Arial,sans-serif;color:var(--ink)}
.abs{position:absolute}
.side{top:82px;bottom:0;width:36px;background:var(--lime)}
.side.left{left:0}.side.right{right:0}
.topbar{left:0;top:36px;width:1176px;height:46px;background:linear-gradient(#3a3a3a,#1c1c1c)}
.find{left:956px;top:13px;font-size:14px}
.social{top:11px;width:19px;height:19px;border-radius:3px}
.brand-mark{left:90px;top:108px;width:26px;height:26px;background:var(--lime)}
.brand-name{left:128px;top:94px;font-size:52px;font-weight:700;line-height:56px;color:var(--ink)}
.nav{top:48px;font-family:"Roboto Condensed",Arial,sans-serif;font-size:19px;color:var(--white)}
.nav.active{color:#c8f04a;text-shadow:0 0 6px #9cc43a}
.date{right:46px;top:92px;text-align:right;color:var(--lime);font-size:22px;line-height:29px}
.date .url{font-size:14px;font-weight:700;line-height:16px;margin-top:2px}
.hero{left:36px;top:178px;width:1104px;height:368px;background:linear-gradient(100deg,#b69066 0%,#d9b98a 20%,#c7462f 38%,#e4a06a 55%,#c8302a 75%,#e9cc8a 100%)}
.arrow{top:340px;width:53px;height:66px;background:#111;display:flex;align-items:center;justify-content:center}
.arrow.prev{left:17px}.arrow.next{left:1105px}
.promo{left:620px;top:240px;width:480px;height:234px;background:rgba(190,215,90,.55);border:2px solid rgba(200,225,90,.9);padding:28px 16px 0;text-align:center;font-family:"Roboto Condensed",Arial,sans-serif;font-size:24px;line-height:29px;color:#222}
.promo .brand{color:var(--white)}
.btn{display:flex;align-items:center;justify-content:center;background:linear-gradient(#b6e04c,#78b01e);border:1px solid #6e9e1a;border-radius:3px;color:#111;font-family:"Roboto Condensed",Arial,sans-serif}
.register{left:755px;top:402px;width:205px;height:55px;font-size:26px;box-shadow:0 2px 4px rgba(0,0,0,.3)}
.headline{left:46px;top:580px;width:760px;text-align:center;font-size:28px;line-height:27px}
.headline .sub{font-style:italic;color:var(--lime);margin-top:4px}
.headline .sub b{font-style:normal;font-weight:400;color:var(--ink)}
.sep{left:36px;top:682px;width:800px;height:24px}
.about-title{left:60px;top:731px;font-size:20px;font-weight:400}
.about{left:58px;top:757px;width:740px;font-size:13.2px;line-height:25px}
.strip{top:936px;height:104px}
.strip.p1{left:56px;width:157px;background:linear-gradient(#c89a52,#7a4a2a)}
.strip.p2{left:213px;width:169px;background:linear-gradient(#c7cfc8,#8a8f7e)}
.strip.p3{left:382px;width:92px;background:linear-gradient(#a9452e,#5a2a1c)}
.strip.p4{left:474px;width:170px;background:linear-gradient(#8fb4c8,#4f7a3a)}
.loves{left:644px;top:936px;width:162px;height:104px;background:var(--lime);color:var(--white);padding:20px 14px}
.loves h3{font-weight:400;font-size:13.5px;color:#111;margin-bottom:12px}
.loves h3 span{color:var(--white)}
.loves p{font-size:10.5px;line-height:15px}
.closing{left:56px;top:1062px;width:740px;font-size:13.2px;line-height:17px}
.divider{left:836px;top:600px;width:1px;height:558px;background:var(--rule)}
.exhibit-title{left:854px;top:587px;font-size:22px;font-weight:400}
.exhibit-title span{color:var(--lime)}
.exhibit-sub{left:878px;top:622px;width:220px;font-size:13.5px;line-height:18px;color:#333}
.photo-a{left:853px;top:667px;width:270px;height:147px;background:linear-gradient(120deg,#e2e4e6,#c47a5a 55%,#b5b9bd)}
.signup{left:852px;top:823px;width:269px;height:42px;font-size:28px}
.side-rule{left:852px;top:882px;width:271px;height:3px;background:#ececec}
.services-title{left:854px;top:903px;font-size:20px;font-weight:400}
.services-sub{left:856px;top:930px;font-size:13.5px;color:#333}
.photo-b{left:852px;top:959px;width:272px;height:146px;background:linear-gradient(120deg,#8a6d55,#e8dcd0 55%,#c9c9c9)}
.more{left:1021px;top:1119px;font-size:13.5px;color:var(--lime);display:flex;align-items:center;gap:6px}
.footer{left:36px;top:1162px;width:1104px;height:38px;background:var(--lime-soft);font-size:11.5px;display:flex;align-items:center;justify-content:center}
</style>
</head>
<body>
<div class="abs side left"></div>
<div class="abs side right"></div>
<div class="abs topbar"></div>

<div class="abs find">Find us on :</div>
<span class="abs social" style="left:1032px;background:#3b5998"></span>
<span class="abs social" style="left:1057px;background:#3aa9e0"></span>
<span class="abs social" style="left:1082px;background:#1c75b0"></span>
<span class="abs social" style="left:1107px;background:#ee8a24"></span>

<span class="abs brand-mark"></span>
<div class="abs brand-name">brisk!</div>

<nav>
  <a class="abs nav active" style="left:576px">Home</a>
  <a class="abs nav" style="left:686px">About us</a>
  <a class="abs nav" style="left:811px">Exhibitors</a>
  <a class="abs nav" style="left:942px">Events</a>
  <a class="abs nav" style="left:1038px">Contact</a>
</nav>

<div class="abs date">6th-7th August 2010,<br>Grand Pavilion of Trades, Harbour Park Sydney<div class="url">www.briskshow.com.au</div></div>

<div class="abs hero" role="img" aria-label="Close-up of a sandwich with lettuce, tomato and ham on wholemeal bread"></div>
<div class="abs arrow prev"><svg width="22" height="36" viewBox="0 0 22 36"><path d="M18 3 4 18l14 15" fill="none" stroke="#fff" stroke-width="4"/></svg></div>
<div class="abs arrow next"><svg width="22" height="36" viewBox="0 0 22 36"><path d="M4 3l14 15L4 33" fill="none" stroke="#fff" stroke-width="4"/></svg></div>

<div class="abs promo"><span class="brand">brisk!</span> brings together worlds most talented sandwich builders for the Toastathon 2012. Join the rendezvous of fun,food and amazing people!!!</div>
<a class="abs btn register">Register Now</a>

<div class="abs headline">Australia’s first dedicated trade event for the food-to-go market.<div class="sub">Lets go <b>brisk!</b> together in 2012</div></div>
<svg class="abs sep" viewBox="0 0 800 24" preserveAspectRatio="none"><path d="M0 20 Q400 -4 800 20" fill="none" stroke="#e2e2e2" stroke-width="3"/></svg>

<h2 class="abs about-title">Whats brisk! all about?</h2>
<p class="abs about">brisk! Australia's first dedicated trade event for the multi-million dollar food-to-go market.brisk! Grand Pavilion of Trades, Harbour Park, Sydney on 6-7 August 2012. brisk! developed in close consultation with leading industry suppliers, retailers and associations.<br>brisk! an unmissable opportunity for owners and managers of quality sandwich bars, juice bars, cafes, restaurants, hotels, delicatessens and contract caterers to source new products and innovations, find out about the latest food-to-go market trends and network with 1000's of industry professionals all in one dedicated arena.</p>

<div class="abs strip p1" role="img" aria-label="Friends chatting at a café table"></div>
<div class="abs strip p2" role="img" aria-label="People sharing food in a kitchen"></div>
<div class="abs strip p3" role="img" aria-label="Hands reaching for a shared platter"></div>
<div class="abs strip p4" role="img" aria-label="Group enjoying a picnic lunch outdoors"></div>
<div class="abs loves"><h3>Everyone loves <span>brisk!</span></h3><p>Tell me more about the<br>Events &#10148;</p></div>

<p class="abs closing">Along with a dedicated brisk! exhibitor zone, the brisk! menu will be packed with tasty features and attractions, including: stimulating speakers, exciting demonstrations, dynamic competitions and informative workshops.</p>

<div class="abs divider"></div>
<h2 class="abs exhibit-title">Want to exhibit at <span>brisk!</span></h2>
<p class="abs exhibit-sub">Be part of this exciting new trade event.Book your stand today!</p>
<div class="abs photo-a" role="img" aria-label="Chef plating a dish in a commercial kitchen"></div>
<a class="abs btn signup">Sign up</a>
<div class="abs side-rule"></div>
<h2 class="abs services-title">Exhibitor Services</h2>
<p class="abs services-sub">Exhibitor forms rules ,deadlines and more</p>
<div class="abs photo-b" role="img" aria-label="Chefs cooking together at a stove"></div>
<a class="abs more">Read More <svg width="16" height="13" viewBox="0 0 16 13"><path d="M0 0l16 6.5L0 13l4-6.5z" fill="#9cc43a"/></svg></a>

<footer class="abs footer">Copyright © 2011 brisk!</footer>
</body>
</html>
```